immediate money for financial solutions

We need a Clean yet, eye catching, Business Card denoting a professional financial/tech firm. The front should have our logo and the notion that we are money lenders that get business loans quickly & easily. Maybe shade the colors of our logo. We are opened, but not committed to an unusual shaped card. The Back Should have our Business Contact Info & logo found on our website's front page: KORVANTINC.COM

Financial

```html
<!DOCTYPE html>
<html lang="en">
<head>
<meta charset="UTF-8">
<title>Korvant Inc — Business Card</title>
<link rel="stylesheet" href="https://fonts.googleapis.com/css2?family=Source+Sans+3:ital,wght@0,400;0,600;0,700;1,400&display=swap">
<style>
  :root {
    --backdrop: #1c1c1c;
    --card-white: #ffffff;
    --card-mint: #f1f7f4;
    --brand-green: #1f9a68;
    --brand-green-deep: #16865a;
    --text-grey: #9aa5a0;
    --text-white: #ffffff;
  }
  * { box-sizing: border-box; margin: 0; padding: 0; }
  html, body {
    width: 1200px;
    height: 873px;
    overflow: hidden;
    background: var(--backdrop);
    font-family: "Source Sans 3", Arial, sans-serif;
  }
  .canvas {
    position: relative;
    width: 1200px;
    height: 873px;
  }
  .card {
    position: absolute;
    top: 286px;
    width: 520px;
    height: 300px;
    overflow: hidden;
    border-radius: 3px;
  }
  .card--contact { left: 50px; background: var(--card-white); }
  .card--brand { left: 630px; background: var(--card-mint); }

  .card__wave {
    position: absolute;
    inset: 0;
    width: 100%;
    height: 100%;
  }
  .contact-block {
    position: absolute;
    left: 44px;
    top: 28px;
    color: var(--brand-green);
  }
  .contact-block__name {
    font-size: 30px;
    font-weight: 700;
    line-height: 1;
  }
  .contact-block__title {
    font-size: 13px;
    font-style: italic;
    line-height: 1.2;
    margin-top: 4px;
  }
  .contact-block__list {
    list-style: none;
    margin-top: 10px;
    font-size: 16px;
    line-height: 20px;
  }
  .contact-block__list li {
    display: flex;
    align-items: center;
    gap: 8px;
  }
  .contact-block__list .icon {
    width: 12px;
    height: 12px;
    flex: none;
  }
  .contact-block__list .indent { padding-left: 20px; }

  .wordmark {
    position: absolute;
    color: var(--brand-green);
    text-align: center;
  }
  .wordmark__row {
    display: flex;
    align-items: center;
    justify-content: center;
    gap: 8px;
    border-bottom: 1.5px solid var(--brand-green);
  }
  .wordmark__name {
    font-weight: 700;
    letter-spacing: 0.02em;
    text-transform: uppercase;
  }
  .wordmark__square {
    background: var(--brand-green);
    flex: none;
  }
  .wordmark__tagline {
    font-weight: 700;
    letter-spacing: 0.08em;
  }

  .wordmark--small { left: 350px; top: 148px; }
  .wordmark--small .wordmark__row { padding-bottom: 2px; }
  .wordmark--small .wordmark__name { font-size: 19px; }
  .wordmark--small .wordmark__square { width: 16px; height: 16px; }
  .wordmark--small .wordmark__tagline { font-size: 11px; margin-top: 2px; }

  .wordmark--large { left: 0; right: 0; top: 96px; display: flex; flex-direction: column; align-items: center; }
  .wordmark--large .wordmark__row { padding: 0 6px 4px; border-bottom-width: 2px; }
  .wordmark--large .wordmark__name { font-size: 40px; }
  .wordmark--large .wordmark__square { width: 32px; height: 32px; }
  .wordmark--large .wordmark__tagline { font-size: 22px; margin-top: 4px; }

  .card__url {
    position: absolute;
    font-size: 15px;
  }
  .card--contact .card__url {
    left: 34px;
    bottom: 22px;
    color: var(--text-white);
    font-size: 20px;
  }
  .card--brand .card__url {
    left: 0;
    right: 0;
    top: 212px;
    text-align: center;
    color: var(--text-grey);
  }
</style>
</head>
<body>
<main class="canvas">

  <section class="card card--contact" aria-label="Contact side">
    <svg class="card__wave" viewBox="0 0 520 300" aria-hidden="true">
      <path d="M0,188 C140,202 280,252 410,300 L0,300 Z" fill="var(--brand-green)"/>
      <path d="M0,172 C150,184 300,238 450,300" fill="none" stroke="var(--brand-green)" stroke-width="2"/>
    </svg>

    <div class="contact-block">
      <h1 class="contact-block__name">Daniel Marsh</h1>
      <p class="contact-block__title">President/Lender</p>
      <ul class="contact-block__list">
        <li>
          <svg class="icon" viewBox="0 0 12 12" aria-hidden="true">
            <circle cx="6" cy="6" r="5.3" fill="none" stroke="var(--brand-green)" stroke-width="1.2"/>
            <path d="M4,3.2 L5,3 L5.6,4.6 L5,5.1 Q5.6,6.5 6.9,7 L7.4,6.4 L9,7 L8.8,8 Q6,8.6 3.9,5.2 Z" fill="var(--brand-green)"/>
          </svg>
          555-014-2276
        </li>
        <li>
          <svg class="icon" viewBox="0 0 12 12" aria-hidden="true">
            <rect x="0.5" y="2" width="11" height="8" fill="var(--brand-green)"/>
            <path d="M0.5,2 L6,6.5 L11.5,2" fill="none" stroke="var(--card-white)" stroke-width="1"/>
          </svg>
          daniel@korvantinc.com
        </li>
        <li class="indent">ATMinfo@korvantinc.com</li>
      </ul>
    </div>

    <div class="wordmark wordmark--small">
      <div class="wordmark__row">
        <span class="wordmark__name">Korvant Inc</span>
        <span class="wordmark__square"></span>
      </div>
      <p class="wordmark__tagline">READY-SET-GO</p>
    </div>

    <p class="card__url">www.korvantinc.com</p>
  </section>

  <section class="card card--brand" aria-label="Brand side">
    <div class="wordmark wordmark--large">
      <div class="wordmark__row">
        <span class="wordmark__name">Korvant Inc</span>
        <span class="wordmark__square"></span>
      </div>
      <p class="wordmark__tagline">READY-SET-GO</p>
    </div>
    <p class="card__url">www.korvantinc.com</p>
  </section>

</main>
</body>
</html>
```